Mabel Lorne Catalog to submit to vendors

We need a catalog made with all of the products in our shop for sales purposes. Our Website is www.mabellorneandfriends.example
Almost all of our products are listed on the website. If you can not take the pictures from the site I can upload them. The descriptions are listed as well. There are three additional products that I will upload. This Catalog will be mailed to stores and should include MSRP Prices.
Updates

Hello There-We are looking for a sales catalog to send to stores in our area. We would like to include MSRP and the end we can add wholesale pricing with minimum orders. Our website is www.mabellorneandfriends.example. There are a few products that haven't been added to the website yet. Where can I upload them and send descriptions?Thank you,Colette Added Thursday, January 21, 2016

Target Market(s)

boutiques and gift shops

Industry/Entity Type

Shop

Font styles to use
Serif
Other font styles liked:
• Noteworthy

Colors
e34297
a64599
6b449b
0255a3

Requirements
Must have
• Color! I would like to organize the catalog by sections. Our premade section and our DIY kits. Maybe we should include Gift sets and put the baskets and gift boxes in one section

```html
<!DOCTYPE html>
<html lang="en">
<head>
<meta charset="utf-8">
<title>Mabel Lorne Catalog – Valentine's Day Collection</title>
<link rel="stylesheet" href="https://fonts.googleapis.com/css2?family=Delius&family=Didact+Gothic&display=swap">
<style>
  :root {
    --pink: #e34297;
    --orchid: #a64599;
    --purple: #6b449b;
    --blue: #0255a3;
    --ink-grey: #5a5560;
    --rule: #6b449b;
    --backdrop: #ecebf0;
    --paper: #ffffff;
    --frost: rgba(255, 255, 255, 0.72);
  }
  * { box-sizing: border-box; margin: 0; padding: 0; }
  html, body {
    width: 1200px; height: 1000px; overflow: hidden;
    background: var(--backdrop);
  }
  .canvas { position: relative; width: 1200px; height: 1000px; }

  .spread {
    position: absolute; left: 37px; top: 298px;
    width: 1138px; height: 402px;
    display: flex;
    box-shadow: 0 4px 12px rgba(60, 50, 80, 0.25);
  }

  /* Left page */
  .cover-page { position: relative; width: 569px; height: 402px; }
  .cover-photo {
    position: absolute; left: 0; top: 0; width: 569px; height: 334px;
    background: linear-gradient(120deg, #8a5a45 0%, #c89a86 30%, #e8d8d2 50%, #b57a6a 70%, #6e4a3e 100%);
  }
  .contents-card {
    position: absolute; left: 90px; top: 18px; width: 377px; height: 296px;
    background: var(--frost); border-radius: 18px;
    padding: 16px 64px 0 24px;
    font-family: "Didact Gothic", sans-serif;
  }
  .contents-heading {
    color: var(--purple); font-size: 12px; font-weight: normal; letter-spacing: .2px;
    padding-left: 9px; border-bottom: 1px solid var(--rule);
    line-height: 16px; white-space: nowrap;
  }
  .contents-list { list-style: none; margin-top: 2px; }
  .contents-list li {
    display: flex; font-size: 11px; color: var(--ink-grey); white-space: nowrap;
    line-height: 17px; height: 17px; border-bottom: 1px solid #b8b0c4;
  }
  .contents-list li::after {
    content: ""; flex: 1; border-bottom: 1px dotted #7a7480;
    margin: 0 0 4px 1px;
  }
  .contents-sections { margin-top: 18px; }
  .contents-sections .contents-heading { padding-left: 12px; margin-bottom: 1px; }

  .slogan-band {
    position: absolute; left: 0; top: 334px; width: 569px; height: 68px;
    background: var(--pink); color: #fff;
    font-family: "Delius", cursive; font-size: 24px;
    display: flex; align-items: center; justify-content: center;
  }

  /* Right page */
  .product-page {
    position: relative; width: 569px; height: 402px; background: var(--paper);
  }
  .section-banner { position: absolute; left: 27px; top: 16px; }
  .section-banner span {
    position: absolute; left: 0; top: 0; width: 530px; height: 46px;
    display: flex; align-items: center; justify-content: center;
    color: #fff; font-family: "Delius", cursive; font-size: 19px; white-space: nowrap;
  }
  .collection-title {
    position: absolute; left: 0; right: 0; top: 72px; text-align: center;
    color: var(--pink); font-family: "Delius", cursive; font-size: 23px; font-weight: normal;
  }
  .product {
    position: absolute; top: 102px; width: 180px; text-align: center;
    font-family: "Delius", cursive;
  }
  .product-photo {
    width: 176px; height: 176px; margin: 0 auto;
    border-radius: 50%; border: 8px solid var(--purple);
  }
  .product-name { color: var(--pink); font-size: 14px; font-weight: normal; line-height: 19px; margin-top: 10px; }
  .product-price { color: var(--purple); font-size: 16px; margin-top: 8px; }
  .cupcake { left: 10px; }
  .cupcake .product-photo { background: radial-gradient(circle at 50% 45%, #fff7ee 0%, #f2e2d4 35%, #e05058 65%, #f5f0ee 100%); }
  .gift-basket { left: 193px; }
  .gift-basket .product-photo { background: radial-gradient(circle at 50% 55%, #e8467a 0%, #f2f0f2 55%, #e0dde4 100%); }
  .gift-basket .product-name { margin-top: 26px; }
  .gift-basket .product-price { margin-top: 10px; }
  .scrub-cubes { left: 376px; }
  .scrub-cubes .product-photo { background: radial-gradient(circle at 60% 45%, #d7eaf2 0%, #9ec8dc 30%, #e2439a 65%, #c93a8a 100%); }
  .footer-band {
    position: absolute; left: 0; bottom: 0; width: 569px; height: 22px;
    background: var(--purple);
  }
</style>
</head>
<body>
<div class="canvas">
  <div class="spread">
    <section class="cover-page">
      <div class="cover-photo" role="img" aria-label="Photo of three smiling girls at a table with a pink gift box of bath products"></div>
      <nav class="contents-card">
        <h2 class="contents-heading">PRE-MADE COLLECTION</h2>
        <ul class="contents-list">
          <li>HOLIDAY COLLECTION</li>
          <li>BATH BOMBS</li>
          <li>LIP BALMS</li>
          <li>BODY BUTTER</li>
          <li>BODY LOTION</li>
          <li>BODY WASH</li>
          <li>METEOR BATH BOMB W/ SURPRISE INSIDE</li>
          <li>SHEA BUTTER HEART SOAPS</li>
          <li>ANTI-BACTERIAL HAND GEL</li>
          <li>ALL-NATURAL BUG SPRAY</li>
          <li>MANI-PEDI SPA BASKET</li>
        </ul>
        <div class="contents-sections">
          <h2 class="contents-heading">DO IT YOURSELF</h2>
          <h2 class="contents-heading">GIFT SET AND BOXES</h2>
        </div>
      </nav>
      <div class="slogan-band">Be Gentle. Be Curious. Be Thankful.</div>
    </section>

    <section class="product-page">
      <div class="section-banner">
        <svg width="530" height="62" viewBox="0 0 530 62" aria-hidden="true">
          <path d="M23 0 H507 A23 23 0 0 1 530 23 V58 L512 46 H23 A23 23 0 0 1 23 0 Z" fill="var(--purple)"/>
        </svg>
        <span>All Natural Pre-Made Product Collection</span>
      </div>
      <h1 class="collection-title">Valentine’s Day Collection</h1>

      <article class="product cupcake">
        <div class="product-photo" role="img" aria-label="Photo of cupcake-shaped soaps and bath bombs in red cups"></div>
        <h3 class="product-name">Soap &amp; Bath Bomb<br>Cupcake Combo</h3>
        <p class="product-price">from $ 6.00</p>
      </article>
      <article class="product gift-basket">
        <div class="product-photo" role="img" aria-label="Photo of a pink gift box with heart soaps and a chevron ribbon"></div>
        <h3 class="product-name">Valentine’s Day Gift<br>Basket</h3>
        <p class="product-price">from $25.00</p>
      </article>
      <article class="product scrub-cubes">
        <div class="product-photo" role="img" aria-label="Photo of a tin of heart-shaped sugar scrub cubes"></div>
        <h3 class="product-name">Heart Shaped Sugar<br>Scrub Cubes</h3>
        <p class="product-price">$8.00</p>
      </article>

      <div class="footer-band"></div>
    </section>
  </div>
</div>
</body>
</html>
```